Visitenkarten-Design für Garten- und Landschaftspflege
Tamuga Vent setzte meine Vorstellungen absolut super um ich kann Ihn nur weiter empfehlen. vielen dank
Zielgruppe
Baumpflege, Baumfällung, Garten und Landschaftspflege meine zielgruppe sind Privatpersonen im alter von 20-100Jahren
Aufgabenstellung
Sehr geehrte Damen und Herren, die visitenkarte sollte die angaben so enthalten wie sie auf der von mir gestallteten Visitenkarten sind ( meine ist kein maß der Dinge). Ich habe mein Logo leider nur als 3.jpg Datei. Das Logo darf im Design erändert werden aber bitte nur Feinheiten ansonsten stehen ihnen alle türen offen um kreativ zu sein.
mit freundlichen Grüßen Holger Banzow

```html
<!DOCTYPE html>
<html lang="de">
<head>
<meta charset="utf-8">
<title>Visitenkarte Banzow Gehölzdienst</title>
<link href="https://fonts.googleapis.com/css2?family=Fira+Sans:wght@400;600&display=swap" rel="stylesheet">
<style>
  :root {
    --page: #ffffff;
    --card: #9dbd3c;
    --card-deep: #8aab36;
    --ink: #0b0b08;
    --shadow: rgba(0, 0, 0, 0.22);
  }
  * { margin: 0; padding: 0; box-sizing: border-box; }
  html, body {
    width: 840px; height: 1200px; overflow: hidden;
    background: var(--page);
    font-family: "Fira Sans", sans-serif;
    color: var(--ink);
  }
  .sheet { position: relative; width: 840px; height: 1200px; }
  .card {
    position: absolute; left: 164px; width: 505px; height: 327px;
    background: var(--card); overflow: hidden;
    box-shadow: 6px 5px 6px var(--shadow);
  }
  .card--front { top: 209px; }
  .card--back { top: 599px; }
  .backdrop {
    position: absolute;
    background: radial-gradient(ellipse at center, var(--card-deep) 0%, var(--card-deep) 45%, rgba(138,171,54,0) 72%);
  }
  .card--front .backdrop { left: -40px; top: 0; width: 400px; height: 327px; }
  .card--back .backdrop { left: 100px; top: 0; width: 420px; height: 327px; }
  .ground {
    position: absolute; left: 0; right: 0; bottom: 0; height: 12px;
    background: var(--card-deep);
  }

  .brand {
    position: absolute; display: flex; align-items: center; white-space: nowrap;
  }
  .brand__mark { flex: none; background: var(--ink); }
  .brand__name { font-weight: 600; line-height: 1; }

  .card--front .brand { left: 222px; top: 118px; gap: 12px; }
  .card--front .brand__mark { width: 30px; height: 30px; }
  .card--front .brand__name { font-size: 19px; }

  .card--back .brand { left: 30px; top: 98px; gap: 9px; }
  .card--back .brand__mark { width: 22px; height: 22px; }
  .card--back .brand__name { font-size: 15px; }

  .person, .contact {
    position: absolute; top: 180px; font-size: 17.5px; line-height: 22.8px;
  }
  .person { left: 46px; }
  .person__name { font-weight: 600; margin-bottom: 22.8px; }
  .contact { left: 204px; }
  .contact p, .person p { white-space: nowrap; }

  .services { position: absolute; left: 213px; top: 95px; width: 250px; }
  .services__title {
    font-size: 20.5px; font-weight: 600; letter-spacing: 3.6px;
    white-space: nowrap; line-height: 26px;
  }
  .rule { height: 2px; background: var(--ink); width: 248px; }
  .services__title + .rule { margin-top: 5px; }
  .services__list {
    list-style: none; margin: 13px 0 13px; font-size: 17.5px; line-height: 21px;
  }
  .services__list li::before { content: "• "; }
  .services__extra { margin-top: 15px; font-size: 16px; line-height: 20px; }
</style>
</head>
<body>
<div class="sheet">

  <section class="card card--front">
    <div class="backdrop" role="img" aria-label="Faint tree silhouette in darker green"></div>
    <div class="ground" role="img" aria-label="Faint grass and fence strip"></div>
    <div class="brand">
      <span class="brand__mark"></span>
      <p class="brand__name">Banzow Gehölzdienst</p>
    </div>
    <div class="person">
      <p class="person__name">Holger Banzow</p>
      <p>Fachagrarwirt</p>
      <p>Baumpflege/</p>
      <p>Baumsanierung</p>
    </div>
    <div class="contact">
      <p>Lindenweg 12</p>
      <p>85599 Grünhausen</p>
      <p>0170 4826153</p>
      <p>www.banzow-gehoelzdienst.de</p>
      <p>kontakt@banzow-gehoelzdienst.de</p>
    </div>
  </section>

  <section class="card card--back">
    <div class="backdrop" role="img" aria-label="Faint tree silhouette in darker green"></div>
    <div class="ground" role="img" aria-label="Faint grass and fence strip"></div>
    <div class="brand">
      <span class="brand__mark"></span>
      <p class="brand__name">Banzow Gehölzdienst</p>
    </div>
    <div class="services">
      <h2 class="services__title">UNSERE LEISTUNGEN</h2>
      <div class="rule"></div>
      <ul class="services__list">
        <li>Beratung</li>
        <li>Kronenpflege &amp; Einkürzung</li>
        <li>Fällung</li>
        <li>Obstbaumschnitt</li>
      </ul>
      <div class="rule"></div>
      <p class="services__extra">Aufbau &amp; Anfertigung von<br>Gartenhäusern nach Maß</p>
    </div>
  </section>

</div>
</body>
</html>
```